Combining web page

We need a PSD webpage design for our PrestaShop store that shows food combining rules, you can see an example that we put here, you can follow the same information and food image combinations. You are just doing the design but the images when implemented on the website will be clickable that goes to product categories, all text and images will be editable.

This is just an example:
http://merrowtonic.com/content/7-food-combining-rules

Target Market(s)

Natural Product and supplement industry

Industry/Entity Type

Store

Number of Pages Required

1 page

Colors

Designer to choose colors to be used in the design.

Requirements
Must have
• 1. Clear images.
• 2. Clear readable text.
• 3. Company name shown Merrow Tonic.
• 4. Follow the food rules as seen on the web page example, but not the same design.
• 5. Logo should be seen.
• 7. All text and images will be editable.
• 8. Make sure the food images are in their proper groups.
• 9. You are not coping the design we gave you but the details have to be the same, copy the text and the image food groups are important, you cannot just put any food in a group, and the combinations are important.
Nice to have
• Here is the website it is for http://merrowtonic.com/

```html
<!DOCTYPE html>
<html lang="en">
<head>
<meta charset="utf-8">
<title>Merrow Tonic – Food Combining Made Easy</title>
<link href="https://fonts.googleapis.com/css2?family=Raleway:wght@600;700;800&family=Lato:wght@400;700&display=swap" rel="stylesheet">
<style>
:root{
  --cream:#fdfbe7;
  --frame-red:#d3141c;
  --frame-gold:#c8a228;
  --green:#3f8c1c;
  --green-dark:#2f7a14;
  --row-tint:#e4f4cf;
  --ink:#222;
  --muted:#555;
  --grid-line:#c9c9c9;
}
*{box-sizing:border-box;margin:0;padding:0}
html,body{width:767px;height:1200px;overflow:hidden;background:var(--cream)}
body{position:relative;font-family:'Lato',sans-serif;color:var(--ink)}
.frame-outer{position:absolute;left:18px;top:18px;width:732px;height:1164px;border:3px solid var(--frame-red)}
.frame-inner{position:absolute;left:26px;top:26px;width:716px;height:1148px;border:1.5px solid var(--frame-gold)}
.intro{position:absolute;top:64px;width:150px;font-size:5.4px;line-height:1.65;color:var(--muted)}
.intro.left{left:48px}.intro.right{left:574px}
.brand{position:absolute;left:0;width:767px;top:40px;text-align:center;font-family:'Raleway',sans-serif;font-weight:800;font-size:24px;color:var(--green)}
.art{position:absolute;border-radius:50%}
.art-hero{left:322px;top:82px;width:138px;height:86px;background:radial-gradient(circle at 50% 45%,#f2b62a,#d63b1e 55%,#5a9a2a 90%);border-radius:40% 40% 30% 30%}
.caption{position:absolute;font-family:'Raleway',sans-serif;font-weight:700;font-size:8px;color:var(--green);text-align:center;width:200px}
.title{position:absolute;left:0;width:767px;text-align:center;font-family:'Raleway',sans-serif;font-weight:800;font-size:17px;color:#1b1b1b;letter-spacing:.2px}
.title.t1{top:193px}.title.t2{top:1052px}
.chart{position:absolute;left:210px;top:227px;width:346px;border:1px solid var(--grid-line);background:#fff}
.chart-head{display:grid;grid-template-columns:154px repeat(9,1fr);height:27px;background:var(--green);color:#fff}
.key{display:flex;align-items:center;gap:6px;padding-left:6px;font-size:4.6px;line-height:1.3}
.key b{font-size:6px}
.key .pair{text-align:center}
.col-h{border-left:1px solid rgba(255,255,255,.4);text-align:center;font-size:4.3px;line-height:1.15;padding-top:2px}
.col-h b{display:block;font-size:5px;margin-bottom:2px}
.group{display:grid;grid-template-columns:154px repeat(9,1fr);height:82px;border-top:1px solid var(--grid-line)}
.group:nth-child(odd){background:var(--row-tint)}
.label{padding:6px 0 0 16px}
.label .num{font-family:'Raleway',sans-serif;font-weight:700;font-size:14px;line-height:1}
.label h3{font-family:'Raleway',sans-serif;font-weight:700;font-size:6.4px;margin:5px 0 6px}
.label .notes{display:grid;grid-template-columns:repeat(4,32px);font-size:4.2px;line-height:1.6;color:var(--muted)}
.cell{border-left:1px solid var(--grid-line);display:grid;grid-template-rows:15px 19px 10px auto;text-align:center;color:#444}
.cell .m{grid-row:3;font-size:7px;line-height:10px}
.cell .above{grid-row:2;font-size:3.6px;line-height:1.5;color:var(--muted)}
.cell .below{grid-row:4;font-size:3.6px;line-height:1.5;color:var(--muted)}
.rule{position:absolute;left:44px;top:1024px;width:680px;border-top:1px solid #cfcfbf}
.principles{position:absolute;top:1088px;width:152px;font-size:5.4px;line-height:1.65;color:var(--muted)}
</style>
</head>
<body>
<div class="frame-outer"></div>
<div class="frame-inner"></div>

<p class="intro left">Sed ut perspiciatis unde omnis iste natus error sit voluptatem accu san tium doloremque laudantium, totam rem aperiam, eaque ipsa quae ab illo inventore veritatis et quasi architecto beatae vitae dic ta sunt expl icabo. Nemo enim ipsam voluptatem quia voluptas sit aspernatur aut odit aut fugit, sed quia consequuntur magni slores eos qui ratione vo luptatem sequi nesc.</p>
<p class="intro right">Sed ut perspiciatis unde omnis iste natus error sit voluptatem accu san tium doloremque laudantium, totam rem aperiam, eaque ipsa quae ab illo inventore veritatis et quasi architecto beatae vitae dic ta sunt expl icabo. Nemo enim ipsam voluptatem quia voluptas sit aspernatur aut odit aut fugit, sed quia consequuntur magni slores eos qui ratione vo luptatem sequi nesc.</p>

<div class="brand">Merrow Tonic</div>
<div class="art art-hero" role="img" aria-label="Illustration of a heap of vegetables and fruits"></div>
<div class="caption" style="left:284px;top:174px">9 Vegetables</div>

<h1 class="title t1">FOOD COMBINING MADE EASY</h1>

<!-- side illustrations -->
<div class="art" role="img" aria-label="Illustration of lemons" style="left:42px;top:248px;width:130px;height:96px;background:radial-gradient(circle,#fbe46a,#e8c52a 70%,#c9a51c)"></div>
<div class="caption" style="left:6px;top:349px">1 Citrus _ Acid Fruits</div>
<div class="art" role="img" aria-label="Illustration of bananas, pineapple, avocado and other fruits" style="left:40px;top:458px;width:154px;height:80px;border-radius:40%;background:linear-gradient(90deg,#f1c53a,#9a6a2a 50%,#d8453a)"></div>
<div class="caption" style="left:6px;top:549px">2 Fruits (sub Acid)</div>
<div class="art" role="img" aria-label="Illustration of a coconut with palm leaves" style="left:34px;top:616px;width:154px;height:130px;border-radius:45%;background:radial-gradient(circle,#f4efe4,#8a5a33 60%,#5b8a3a)"></div>
<div class="caption" style="left:6px;top:748px">3 Sweet Fruits - Palm Fruits</div>
<div class="art" role="img" aria-label="Illustration of assorted nuts and seeds" style="left:58px;top:842px;width:96px;height:98px;background:radial-gradient(circle,#b7773e,#8a5027 70%,#6a3c1e)"></div>
<div class="caption" style="left:6px;top:948px">4 Neutral Fruits - Raw Nuts - Seeds</div>

<div class="art" role="img" aria-label="Illustration of breads and a croissant" style="left:594px;top:228px;width:130px;height:116px;border-radius:40%;background:radial-gradient(circle,#d9a15c,#a5622b 60%,#6e3d1c)"></div>
<div class="caption" style="left:562px;top:349px">5 Grains</div>
<div class="art" role="img" aria-label="Illustration of pea pods, beans and sprouts" style="left:608px;top:416px;width:104px;height:116px;border-radius:40%;background:radial-gradient(circle,#b4c67a,#7f9a45 65%,#c9b27a)"></div>
<div class="caption" style="left:562px;top:549px">6 Legumes (dry) - Sprouts</div>
<div class="art" role="img" aria-label="Illustration of melon and watermelon slices" style="left:568px;top:608px;width:160px;height:128px;border-radius:40%;background:radial-gradient(circle,#f0a35a,#d8584a 50%,#5b8a3a)"></div>
<div class="caption" style="left:562px;top:748px">7 Melons</div>
<div class="art" role="img" aria-label="Illustration of tomatoes" style="left:588px;top:856px;width:144px;height:88px;border-radius:45%;background:radial-gradient(circle,#f05a3e,#c81e1e 65%,#3f7a2a)"></div>
<div class="caption" style="left:562px;top:948px">8 Succulent Food - Tomatoes</div>

<section class="chart">
  <div class="chart-head">
    <div class="key"><b>KEY:</b><span class="pair">xx Combines well<br>x Fair Compatibility</span><span class="pair">NR Not Recommended<br>No Not Compatible</span></div>
    <div class="col-h"><b>1</b>Citrus Acid</div>
    <div class="col-h"><b>2</b>Fruits</div>
    <div class="col-h"><b>3</b>Palm Fruits</div>
    <div class="col-h"><b>4</b>Natural Fruits</div>
    <div class="col-h"><b>5</b>Grains</div>
    <div class="col-h"><b>6</b>Legumes</div>
    <div class="col-h"><b>7</b>Melons</div>
    <div class="col-h"><b>8</b>Tomatoes</div>
    <div class="col-h"><b>9</b>Veg</div>
  </div>

  <div>
    <div class="group">
      <div class="label"><div class="num">1</div><h3>Citrus _ Acid Fruits</h3>
        <div class="notes"><span>Erspiciatis<br>Unde omnis<br>Iste natusvolu<br>Ptatem accus<br>Antium dolore</span><span>Erspiciatis<br>Unde omn<br>Iste natusv<br>Ptatem acc<br>Antium dol</span><span>Erspicia<br>Unde om<br>Iste natusv<br>Ptatem ac<br>Antium dol</span></div></div>
      <div class="cell"><span class="m">XX</span></div><div class="cell"><span class="m">XX</span></div>
      <div class="cell"><span class="above">xx archite<br>xx archite<br>xx archite</span><span class="m">X</span></div>
      <div class="cell"><span class="m">XX</span></div>
      <div class="cell"><span class="m">NR</span><span class="below">x archite<br>x archite</span></div>
      <div class="cell"><span class="m">X-NR</span><span class="below">x archite<br>x archite</span></div>
      <div class="cell"><span class="m">x</span><span class="below">x archite<br>x archite</span></div>
      <div class="cell"><span class="m">NO</span><span class="below">x archite</span></div>
      <div class="cell"><span class="m">NO</span><span class="below">x archite</span></div>
    </div>
    <div class="group">
      <div class="label"><div class="num">2</div><h3>Fruits (Sub - Acid)</h3>
        <div class="notes"><span>Erspiciatis<br>Unde omnis<br>Iste natusvolu<br>Ptatem accus<br>Antium dolore</span><span>Erspiciatis<br>Unde omn<br>Iste natusv<br>Ptatem acc<br>Antium dol</span><span>Erspicia<br>Unde om<br>Iste natusv<br>Ptatem ac<br>Antium dol</span><span>Erspicia<br>Unde om<br>Iste natusv<br>Ptatem ac<br>Antium dol</span></div></div>
      <div class="cell"><span class="m">XX</span></div><div class="cell"><span class="m">XX</span></div>
      <div class="cell"><span class="above">xx archite<br>xx archite<br>xx archite</span><span class="m">X</span></div>
      <div class="cell"><span class="m">XX</span></div>
      <div class="cell"><span class="m">NR</span><span class="below">x archite<br>x archite</span></div>
      <div class="cell"><span class="m">X-NR</span><span class="below">x archite<br>x archite</span></div>
      <div class="cell"><span class="m">x</span><span class="below">x archite<br>x archite</span></div>
      <div class="cell"><span class="m">NO</span><span class="below">x archite</span></div>
      <div class="cell"><span class="m">NO</span><span class="below">x archite</span></div>
    </div>
    <div class="group">
      <div class="label"><div class="num">3</div><h3>Sweet Fruits - Palm Fruits</h3>
        <div class="notes"><span>Erspiciatis<br>Unde omnis<br>Iste natusvolu<br>Ptatem accus<br>Antium dolore</span><span>Erspiciatis<br>Unde omn<br>Iste natusv<br>Ptatem acc<br>Antium dol</span><span>Erspicia<br>Unde om<br>Iste natusv<br>Ptatem ac<br>Antium dol</span></div></div>
      <div class="cell"><span class="m">XX</span></div><div class="cell"><span class="m">XX</span></div>
      <div class="cell"><span class="above">xx archite<br>xx archite<br>xx archite</span><span class="m">X</span></div>
      <div class="cell"><span class="m">XX</span></div>
      <div class="cell"><span class="m">NR</span><span class="below">x archite<br>x archite</span></div>
      <div class="cell"><span class="m">X-NR</span><span class="below">x archite<br>x archite</span></div>
      <div class="cell"><span class="m">x</span><span class="below">x archite<br>x archite</span></div>
      <div class="cell"><span class="m">NO</span><span class="below">x archite</span></div>
      <div class="cell"><span class="m">NO</span><span class="below">x archite</span></div>
    </div>
    <div class="group">
      <div class="label"><div class="num">4</div><h3>Neutral Fruits - Raw Nuts - Seeds</h3>
        <div class="notes"><span>Erspiciatis<br>Unde omnis<br>Iste natusvolu<br>Ptatem accus<br>Antium dolore</span><span>Erspiciatis<br>Unde omn<br>Iste natusv<br>Ptatem acc<br>Antium dol</span><span>Erspicia<br>Unde om<br>Iste natusv<br>Ptatem ac<br>Antium dol</span><span>Erspicia<br>Unde om<br>Iste natusv<br>Ptatem ac<br>Antium dol</span></div></div>
      <div class="cell"><span class="m">XX</span></div><div class="cell"><span class="m">XX</span></div>
      <div class="cell"><span class="above">xx archite<br>xx archite<br>xx archite</span><span class="m">X</span></div>
      <div class="cell"><span class="m">XX</span></div>
      <div class="cell"><span class="m">NR</span><span class="below">x archite<br>x archite</span></div>
      <div class="cell"><span class="m">X-NR</span><span class="below">x archite<br>x archite</span></div>
      <div class="cell"><span class="m">x</span><span class="below">x archite<br>x archite</span></div>
      <div class="cell"><span class="m">NO</span><span class="below">x archite</span></div>
      <div class="cell"><span class="m">NO</span><span class="below">x archite</span></div>
    </div>
    <div class="group">
      <div class="label"><div class="num">5</div><h3>Grains</h3>
        <div class="notes"><span>Erspiciatis<br>Unde omnis<br>Iste natusvolu<br>Ptatem accus<br>Antium dolore</span><span>Erspiciatis<br>Unde omn<br>Iste natusv<br>Ptatem acc<br>Antium dol</span><span>Erspicia<br>Unde om<br>Iste natusv<br>Ptatem ac<br>Antium dol</span></div></div>
      <div class="cell"><span class="m">XX</span></div><div class="cell"><span class="m">XX</span></div>
      <div class="cell"><span class="above">xx archite<br>xx archite<br>xx archite</span><span class="m">X</span></div>
      <div class="cell"><span class="m">XX</span></div>
      <div class="cell"><span class="m">NR</span><span class="below">x archite<br>x archite</span></div>
      <div class="cell"><span class="m">X-NR</span><span class="below">x archite<br>x archite</span></div>
      <div class="cell"><span class="m">x</span><span class="below">x archite<br>x archite</span></div>
      <div class="cell"><span class="m">NO</span><span class="below">x archite</span></div>
      <div class="cell"><span class="m">NO</span><span class="below">x archite</span></div>
    </div>
    <div class="group">
      <div class="label"><div class="num">6</div><h3>Legumes (dry) - Sprouts</h3>
        <div class="notes"><span>Erspiciatis<br>Unde omnis<br>Iste natusvolu<br>Ptatem accus<br>Antium dolore</span><span>Erspiciatis<br>Unde omn<br>Iste natusv<br>Ptatem acc<br>Antium dol</span><span>Erspicia<br>Unde om<br>Iste natusv<br>Ptatem ac<br>Antium dol</span><span>Erspicia<br>Unde om<br>Iste natusv<br>Ptatem ac<br>Antium dol</span></div></div>
      <div class="cell"><span class="m">XX</span></div><div class="cell"><span class="m">XX</span></div>
      <div class="cell"><span class="above">xx archite<br>xx archite<br>xx archite</span><span class="m">X</span></div>
      <div class="cell"><span class="m">XX</span></div>
      <div class="cell"><span class="m">NR</span><span class="below">x archite<br>x archite</span></div>
      <div class="cell"><span class="m">X-NR</span><span class="below">x archite<br>x archite</span></div>
      <div class="cell"><span class="m">x</span><span class="below">x archite<br>x archite</span></div>
      <div class="cell"><span class="m">NO</span><span class="below">x archite</span></div>
      <div class="cell"><span class="m">NO</span><span class="below">x archite</span></div>
    </div>
    <div class="group">
      <div class="label"><div class="num">7</div><h3>Melons</h3>
        <div class="notes"><span>Erspiciatis<br>Unde omnis<br>Iste natusvolu<br>Ptatem accus<br>Antium dolore</span><span>Erspiciatis<br>Unde omn<br>Iste natusv<br>Ptatem acc<br>Antium dol</span><span>Erspicia<br>Unde om<br>Iste natusv<br>Ptatem ac<br>Antium dol</span></div></div>
      <div class="cell"><span class="m">XX</span></div><div class="cell"><span class="m">XX</span></div>
      <div class="cell"><span class="above">xx archite<br>xx archite<br>xx archite</span><span class="m">X</span></div>
      <div class="cell"><span class="m">XX</span></div>
      <div class="cell"><span class="m">NR</span><span class="below">x archite<br>x archite</span></div>
      <div class="cell"><span class="m">X-NR</span><span class="below">x archite<br>x archite</span></div>
      <div class="cell"><span class="m">x</span><span class="below">x archite<br>x archite</span></div>
      <div class="cell"><span class="m">NO</span><span class="below">x archite</span></div>
      <div class="cell"><span class="m">NO</span><span class="below">x archite</span></div>
    </div>
    <div class="group">
      <div class="label"><div class="num">8</div><h3>Succulent Food - Tomatoes</h3>
        <div class="notes"><span>Erspiciatis<br>Unde omnis<br>Iste natusvolu<br>Ptatem accus<br>Antium dolore</span><span>Erspiciatis<br>Unde omn<br>Iste natusv<br>Ptatem acc<br>Antium dol</span><span>Erspicia<br>Unde om<br>Iste natusv<br>Ptatem ac<br>Antium dol</span><span>Erspicia<br>Unde om<br>Iste natusv<br>Ptatem ac<br>Antium dol</span></div></div>
      <div class="cell"><span class="m">XX</span></div><div class="cell"><span class="m">XX</span></div>
      <div class="cell"><span class="above">xx archite<br>xx archite<br>xx archite</span><span class="m">X</span></div>
      <div class="cell"><span class="m">XX</span></div>
      <div class="cell"><span class="m">NR</span><span class="below">x archite<br>x archite</span></div>
      <div class="cell"><span class="m">X-NR</span><span class="below">x archite<br>x archite</span></div>
      <div class="cell"><span class="m">x</span><span class="below">x archite<br>x archite</span></div>
      <div class="cell"><span class="m">NO</span><span class="below">x archite</span></div>
      <div class="cell"><span class="m">NO</span><span class="below">x archite</span></div>
    </div>
    <div class="group">
      <div class="label"><div class="num">9</div><h3>Vegetables</h3>
        <div class="notes"><span>Erspiciatis<br>Unde omnis<br>Iste natusvolu<br>Ptatem accus<br>Antium dolore</span><span>Erspiciatis<br>Unde omn<br>Iste natusv<br>Ptatem acc<br>Antium dol</span><span>Erspicia<br>Unde om<br>Iste natusv<br>Ptatem ac<br>Antium dol</span></div></div>
      <div class="cell"><span class="m">XX</span></div><div class="cell"><span class="m">XX</span></div>
      <div class="cell"><span class="above">xx archite<br>xx archite<br>xx archite</span><span class="m">X</span></div>
      <div class="cell"><span class="m">XX</span></div>
      <div class="cell"><span class="m">NR</span><span class="below">x archite<br>x archite</span></div>
      <div class="cell"><span class="m">X-NR</span><span class="below">x archite<br>x archite</span></div>
      <div class="cell"><span class="m">x</span><span class="below">x archite<br>x archite</span></div>
      <div class="cell"><span class="m">NO</span><span class="below">x archite</span></div>
      <div class="cell"><span class="m">NO</span><span class="below">x archite</span></div>
    </div>
  </div>
</section>

<div class="rule"></div>
<h2 class="title t2">PRINCIPLES OF EATING</h2>
<p class="principles" style="left:48px">Sed ut perspiciatis unde omnis iste natus error sit voluptatem accu san tium doloremque laudantium, totam rem aperiam, eaque ipsa quae ab illo inventore veritatis et quasi architecto beatae vitae dic ta sunt expl icabo. Nemo enim ipsam voluptatem quia voluptas sit aspernatur aut odit aut fugit, sed quia consequuntur magni slores eos qui ratione vo luptatem sequi nesc.</p>
<p class="principles" style="left:223px">Sed ut perspiciatis unde omnis iste natus error sit voluptatem accu san tium doloremque laudantium, totam rem aperiam, eaque ipsa quae ab illo inventore veritatis et quasi architecto beatae vitae dic ta sunt expl icabo. Nemo enim ipsam voluptatem quia voluptas sit aspernatur aut odit aut fugit, sed quia consequuntur magni slores eos qui ratione vo luptatem sequi nesc.</p>
<p class="principles" style="left:398px">Sed ut perspiciatis unde omnis iste natus error sit voluptatem accu san tium doloremque laudantium, totam rem aperiam, eaque ipsa quae ab illo inventore veritatis et quasi architecto beatae vitae dic ta sunt expl icabo. Nemo enim ipsam voluptatem quia voluptas sit aspernatur aut odit aut fugit, sed quia consequuntur magni slores eos qui ratione vo luptatem sequi nesc.</p>
<p class="principles" style="left:574px">Sed ut perspiciatis unde omnis iste natus error sit voluptatem accu san tium doloremque laudantium, totam rem aperiam, eaque ipsa quae ab illo inventore veritatis et quasi architecto beatae vitae dic ta sunt expl icabo. Nemo enim ipsam voluptatem quia voluptas sit aspernatur aut odit aut fugit, sed quia consequuntur magni slores eos qui ratione vo luptatem sequi nesc.</p>
</body>
</html>
```